RW Business Card Design

My company provides advising/training and coaching services to business owners who want better financial results and better work/life balance. We help them through creating custom plans supported with education, strategic thinking and accountability.

We also help through some online courses which are geared to smaller businesses.
Updates

please also include our nth american contact # +1 555 208 4471

Industry/Entity Type

Financial

Contact Information for Business Card

Morgan Halberd
morgan@morganhalberd-example.com
+61 400 555 917
www.morganhalberd-example.com

```html
<!DOCTYPE html>
<html lang="en">
<head>
<meta charset="utf-8">
<title>Morgan Halberd – Business Card</title>
<link href="https://fonts.googleapis.com/css2?family=Arimo:wght@400;700&display=swap" rel="stylesheet">
<style>
  :root {
    --page-bg: #e9e6e2;
    --card-bg: #ffffff;
    --brand-blue: #1f7fc3;
    --brand-grey: #9b9b9b;
    --card-shadow: rgba(60, 40, 20, 0.18);
  }
  * { box-sizing: border-box; margin: 0; padding: 0; }
  html, body {
    width: 1200px;
    height: 914px;
    overflow: hidden;
    background: var(--page-bg);
    font-family: "Arimo", Arial, sans-serif;
  }
  .canvas {
    position: relative;
    width: 1200px;
    height: 914px;
  }
  .card {
    position: absolute;
    width: 580px;
    height: 332px;
    background: var(--card-bg);
    box-shadow: 0 6px 22px var(--card-shadow);
  }
  .card--back { top: 110px; right: 90px; }
  .card--front { top: 480px; left: 90px; }

  .brand {
    display: flex;
    align-items: center;
    gap: 14px;
  }
  .brand__dot {
    width: 34px;
    height: 34px;
    border-radius: 50%;
    background: var(--brand-blue);
    flex: none;
  }
  .brand__name {
    color: var(--brand-blue);
    font-weight: 400;
    font-size: 30px;
    letter-spacing: 0.5px;
    text-transform: uppercase;
    white-space: nowrap;
  }

  .card--back .brand {
    position: absolute;
    top: 112px;
    left: 92px;
  }
  .tagline {
    position: absolute;
    top: 190px;
    left: 92px;
    color: var(--brand-blue);
    font-size: 19px;
    white-space: nowrap;
  }
  .tagline__result { font-weight: 700; margin-left: 8px; }

  .card--front .brand {
    position: absolute;
    top: 44px;
    left: 52px;
  }
  .contact-list {
    position: absolute;
    top: 150px;
    left: 52px;
    list-style: none;
  }
  .contact-list li {
    display: flex;
    align-items: center;
    gap: 18px;
    height: 30px;
    color: var(--brand-blue);
    font-size: 19px;
  }
  .contact-icon {
    width: 16px;
    height: 16px;
    flex: none;
    fill: none;
    stroke: var(--brand-blue);
    stroke-width: 1.6;
  }
  .contact-icon--solid { fill: var(--brand-blue); stroke: none; }
</style>
</head>
<body>
<main class="canvas">

  <section class="card card--back" aria-label="Business card, back">
    <div class="brand">
      <span class="brand__dot"></span>
      <span class="brand__name">Morgan Halberd</span>
    </div>
    <p class="tagline">Knowledge + Planning * Action =<span class="tagline__result">Success</span></p>
  </section>

  <section class="card card--front" aria-label="Business card, front">
    <div class="brand">
      <span class="brand__dot"></span>
      <span class="brand__name">Morgan Halberd</span>
    </div>
    <ul class="contact-list">
      <li>
        <svg class="contact-icon contact-icon--solid" viewBox="0 0 16 16" aria-hidden="true"><path d="M4 1h3l1 4-2 1.5c.8 1.7 2 3 3.5 3.5L11 8l4 1v3c0 1-1 2-2 2C7 14 2 9 2 3c0-1 1-2 2-2z"/></svg>
        <span>+1 555 208 4471</span>
      </li>
      <li>
        <svg class="contact-icon contact-icon--solid" viewBox="0 0 16 16" aria-hidden="true"><path d="M4 1h3l1 4-2 1.5c.8 1.7 2 3 3.5 3.5L11 8l4 1v3c0 1-1 2-2 2C7 14 2 9 2 3c0-1 1-2 2-2z"/></svg>
        <span>+61 400 555 917</span>
      </li>
      <li>
        <svg class="contact-icon" viewBox="0 0 16 16" aria-hidden="true"><rect x="1.5" y="3.5" width="13" height="9"/><path d="M1.5 3.5l6.5 5 6.5-5"/></svg>
        <span>morgan@morganhalberd-example.com</span>
      </li>
      <li>
        <svg class="contact-icon" viewBox="0 0 16 16" aria-hidden="true"><circle cx="8" cy="8" r="6.5"/><path d="M1.5 8h13M8 1.5c-2.5 3-2.5 10 0 13M8 1.5c2.5 3 2.5 10 0 13"/></svg>
        <span>www.morganhalberd-example.com</span>
      </li>
    </ul>
  </section>

</main>
</body>
</html>
```